Zenfro loop flyer

I want this flyer to look like the one I upload here called zenfro loop. I want the to change to words (headline):"A new category in pet hydration" to: Ny unik produkt i Kategori hund. Also remove Functional elektrodryck för hundar.
Also change:" Vi tar emot Återförsäljarpartners" to "Kontakta oss för mer information"
If you think or see improvments plase do so. Its for a launch of a newe product to retailers (so not to the consumer).

Target Market(s)

Retail, stores, hotels, restaurants

Industry/Entity Type

Energy water for dogs

Colors
0054AA
0677BA
7BADD7
CADEEF
E8F1F8

Requirements
Must have
• Think grimvolt, quorza pell, energy drinks but for dogs

```html
<!DOCTYPE html>
<html lang="sv">
<head>
<meta charset="utf-8">
<title>Zenfro loop – återförsäljarflyer</title>
<link href="https://fonts.googleapis.com/css2?family=Anton&family=Figtree:wght@400;600;700;800&display=swap" rel="stylesheet">
<style>
  :root{
    --navy:#1c1464;
    --gold:#c19a5b;
    --gold-light:#e6c873;
    --footer:#0f1630;
    --ink:#1d1d2b;
    --red:#a83a3a;
    --icon-dark:#0f1a33;
    --card:#eaf1fb;
    --card-head:#e4d3b0;
    --blue:#0054aa;
    --blue-mid:#0677ba;
    --blue-soft:#7badd7;
    --stage:#6b6b6b;
    --white:#ffffff;
  }
  *{margin:0;padding:0;box-sizing:border-box}
  html,body{width:1200px;height:1200px;overflow:hidden;background:var(--stage)}
  body{font-family:"Figtree",sans-serif;color:var(--ink)}
  .flyer{position:absolute;left:190px;top:20px;width:820px;height:1160px;background:var(--white);overflow:hidden}
  .abs{position:absolute}

  /* header */
  .brand{left:40px;top:40px;display:flex;align-items:center;gap:10px}
  .brand-mark{width:34px;height:34px;background:var(--navy)}
  .brand-name{font-weight:800;font-size:25px;color:var(--navy);line-height:1}
  .header-rule{left:218px;top:42px;width:2px;height:48px;background:var(--navy)}
  .tagline{left:239px;top:52px;font-weight:700;font-size:14px;line-height:17px;color:var(--navy)}
  .origin-badge{left:664px;top:0;width:122px;height:124px;background:var(--navy);border-radius:0 0 18px 18px;text-align:center;padding-top:38px}
  .origin-badge p{font-weight:700;font-size:14.5px;line-height:19px;color:var(--gold)}
  .origin-badge svg{margin-top:6px}

  /* headline */
  .headline{left:40px;top:156px;font-family:"Anton",sans-serif;font-size:77px;line-height:71px;letter-spacing:-1px;color:var(--navy)}
  .headline .accent{color:var(--gold)}

  /* product */
  .product-visual{left:326px;top:191px;width:213px;height:759px;border-radius:60px 60px 30px 30px;
    background:linear-gradient(180deg,#eef3f8 0%,#ffffff 18%,#1d3fb5 35%,#20309a 60%,#f4f7fb 62%,#e8eef5 100%)}

  /* reasons */
  .reasons-title{left:40px;top:489px;font-weight:700;font-size:20px;line-height:23.5px;color:var(--navy);letter-spacing:.3px}
  .rule-gold{height:2px;width:62px;background:var(--gold)}
  .reason{left:34px;display:flex;gap:12px;width:300px}
  .reason .ring{flex:none;width:40px;height:40px;border:1.2px solid #c9c9cf;border-radius:50%;display:flex;align-items:center;justify-content:center}
  .reason h3{font-weight:700;font-size:12.5px;line-height:15px;color:var(--gold)}
  .reason p{font-size:12.5px;line-height:14.5px;margin-top:4px;color:var(--ink)}

  /* benefits */
  .pitch{left:553px;top:164px;width:240px;font-weight:700;font-size:18.5px;line-height:22px;color:var(--navy)}
  .benefit{left:550px;display:flex;gap:13px;width:245px}
  .benefit .dot{flex:none;width:58px;height:58px;border-radius:50%;display:flex;align-items:center;justify-content:center}
  .benefit h3{font-weight:700;font-size:14px;line-height:16.5px;color:var(--navy)}
  .benefit p{font-size:13px;line-height:17px;margin-top:8px}
  .benefit.gold h3{color:var(--gold)}
  .soft-rule{left:620px;width:160px;height:1px;background:linear-gradient(90deg,transparent,#bfc3cc,transparent)}

  /* category card */
  .category-card{left:603px;top:671px;width:183px;height:231px;border-radius:14px;background:var(--card);overflow:hidden}
  .category-card h4{background:var(--card-head);height:42px;display:flex;align-items:center;justify-content:center;font-weight:700;font-size:14px;color:var(--navy)}
  .category-card p{padding:12px 10px 0 11px;font-weight:600;font-size:11.7px;line-height:14.7px;color:var(--navy)}
  .category-card svg{display:block;margin:14px auto 0}
  .category-card .foot{text-align:center;font-weight:700;font-size:11.5px;line-height:14.5px;color:var(--navy);margin-top:14px}

  /* footer */
  .footer{left:0;top:953px;width:820px;height:207px;background:var(--footer)}
  .slogan{left:40px;top:953px;width:735px;height:42px;border-radius:0 0 16px 16px;
    background:linear-gradient(90deg,#c9a453,#f1d98a 45%,#c9a453);display:flex;align-items:center;justify-content:center;
    font-weight:800;font-size:16px;color:var(--footer);letter-spacing:.2px}
  .contact-title{left:40px;top:1014px;font-weight:800;font-size:31px;line-height:29px;color:var(--gold)}
  .contact-sub{left:40px;top:1090px;font-size:13.5px;color:#e4e6ee}
  .footer-rule{top:1025px;width:1.5px;height:110px;background:var(--gold)}
  .contacts{left:363px;top:1016px;list-style:none}
  .contacts li{display:flex;align-items:center;gap:14px;height:37px;font-weight:600;font-size:14px;color:var(--white)}
  .launch-label{left:598px;top:1017px;width:188px;text-align:center;font-weight:800;font-size:11.5px;color:var(--white)}
  .launch-box{left:597px;top:1039px;width:189px;height:39px;background:linear-gradient(90deg,#c9a453,#f0d88a,#c9a453);
    display:flex;align-items:center;justify-content:center;font-family:"Anton",sans-serif;font-size:26px;color:var(--footer)}
  .launch-note{left:613px;top:1092px;font-weight:600;font-size:11.5px;line-height:15px;color:var(--white)}
</style>
</head>
<body>
<main class="flyer">

  <header>
    <div class="abs brand"><span class="brand-mark"></span><span class="brand-name">Zenfro loop</span></div>
    <div class="abs header-rule"></div>
    <p class="abs tagline">FUNCTIONAL HYDRATION<br>FÖR HUNDAR</p>
    <div class="abs origin-badge">
      <p>TILLVERKAD I<br>SVERIGE</p>
      <svg width="44" height="28" viewBox="0 0 44 28" aria-label="Svensk flagga"><rect width="44" height="28" fill="#1f5fb0"/><rect x="13" width="7" height="28" fill="#f1c21b"/><rect y="10.5" width="44" height="7" fill="#f1c21b"/></svg>
    </div>
  </header>

  <h1 class="abs headline">NY UNIK<br>PRODUKT I<br><span class="accent">KATEGORI<br>HUND</span></h1>

  <div class="abs product-visual" role="img" aria-label="Produktfoto: 500 ml flaska elektrolytvatten för hundar med blå etikett, stående i vattenstänk"></div>

  <section>
    <h2 class="abs reasons-title">VARFÖR<br>ÅTERFÖRSÄLJARE<br>VÄLJER ZENFRO LOOP</h2>
    <div class="abs rule-gold" style="left:40px;top:570px"></div>

    <div class="abs reason" style="top:601px">
      <span class="ring"><svg width="22" height="16" viewBox="0 0 22 16" fill="none" stroke="#8d8f99" stroke-width="1.4"><path d="M1 15h20M2 12l6-6 4 3 7-7M15 2h4v4"/></svg></span>
      <div><h3>HÖG MARGINAL,<br>LITEN KONKURRENS</h3><p>Var först på en växande<br>kategori.</p></div>
    </div>
    <div class="abs reason" style="top:680px">
      <span class="ring"><svg width="22" height="18" viewBox="0 0 22 18" fill="none" stroke="#8d8f99" stroke-width="1.4"><path d="M1 1h3l3 11h11l2-8H6"/><circle cx="9" cy="16" r="1.3"/><circle cx="16" cy="16" r="1.3"/></svg></span>
      <div><h3>SNABBT VÄXANDE SEGMENT<br>INOM HUNDHÄLSA</h3><p>Stark och ökande efterfrågan<br>från medvetna hundägare.</p></div>
    </div>
    <div class="abs reason" style="top:760px">
      <span class="ring"><svg width="22" height="20" viewBox="0 0 22 20" fill="none" stroke="#8d8f99" stroke-width="1.4"><path d="M11 18S2 12 2 6.5A4.5 4.5 0 0 1 11 4a4.5 4.5 0 0 1 9 2.5C20 12 11 18 11 18z"/></svg></span>
      <div><h3>STOR<br>IMPULSKÖPSPOTENTIAL</h3><p>Perfekt att placera vid<br>vatten och snacks.</p></div>
    </div>
    <div class="abs reason" style="top:843px">
      <span class="ring"><svg width="22" height="22" viewBox="0 0 22 22" fill="none" stroke="#8d8f99" stroke-width="1.4"><path d="M12 2h8v8L10 20 2 12z"/><circle cx="16" cy="6" r="1.3"/></svg></span>
      <div><h3>PREMIUMPOSITIONERING<br>= HÖGRE KUNDVÄRDE</h3><p>Ger mer värde i varje<br>besök.</p></div>
    </div>
  </section>

  <section>
    <p class="abs pitch">Utvecklad för alla hundar. Inspirerad av human sportdryck.</p>
    <div class="abs rule-gold" style="left:553px;top:238px;width:56px"></div>

    <div class="abs benefit" style="top:268px">
      <span class="dot" style="background:var(--icon-dark)"><svg width="24" height="30" viewBox="0 0 24 30" fill="none" stroke="#fff" stroke-width="1.6"><path d="M12 2C12 2 3 13 3 19a9 9 0 0 0 18 0C21 13 12 2 12 2z"/><path d="M9 22c1-4 4-6 7-6-1 4-3 6-7 6z"/></svg></span>
      <div><h3>NATURLIGA<br>ELEKTROLYTER</h3><p>Återställer vätska och<br>stödjer balansen.</p></div>
    </div>
    <div class="abs soft-rule" style="top:352px"></div>
    <div class="abs benefit" style="top:376px">
      <span class="dot" style="background:var(--red)"><svg width="26" height="30" viewBox="0 0 26 30" fill="none" stroke="#fff" stroke-width="1.6"><path d="M13 2S6 11 6 16a7 7 0 0 0 14 0C20 11 13 2 13 2z"/><path d="M2 25c4 3 18 3 22 0"/></svg></span>
      <div><h3>STÖDJER HYDRERING<br>&amp; ÅTERHÄMTNING</h3><p>Hjälper till att upprätthålla prestationsförmåga och välmående.</p></div>
    </div>
    <div class="abs soft-rule" style="top:476px"></div>
    <div class="abs benefit gold" style="top:498px">
      <span class="dot" style="background:var(--gold)" role="img" aria-label="Ikon: aktiv hund"></span>
      <div><h3>PERFEKT EFTER<br>AKTIVITET, VÄRME &amp;<br>RESA</h3><p>För vardagens äventyr<br>och särskilda tillfällen.</p></div>
    </div>

    <div class="abs category-card">
      <h4>KATEGORIMÖJLIGHET</h4>
      <p>Hundhydrering för hundar är ett outnyttjat segment med stor tillväxtpotential.</p>
      <svg width="60" height="52" viewBox="0 0 60 52" aria-label="Växande stapeldiagram">
        <rect x="4" y="40" width="9" height="9" fill="#2c5cc5"/><rect x="18" y="33" width="9" height="16" fill="#2c5cc5"/>
        <rect x="32" y="26" width="9" height="23" fill="#2c5cc5"/><rect x="46" y="16" width="9" height="33" fill="#2c5cc5"/>
        <path d="M2 32C20 28 34 18 50 4" fill="none" stroke="#2c5cc5" stroke-width="3"/><path d="M42 3l10-1-2 10z" fill="#2c5cc5"/>
      </svg>
      <p class="foot">VÄXANDE EFTERFRÅGAN<br>I HELA EUROPA</p>
    </div>
  </section>

  <footer>
    <div class="abs footer"></div>
    <div class="abs slogan">RENA INGREDIENSER. VERKLIGA FÖRDELAR. HUNDAR KÄNNER SKILLNADEN.</div>
    <h2 class="abs contact-title">Kontakta oss för<br>mer information</h2>
    <p class="abs contact-sub">Bli en del av framtidens hundhydrering.</p>
    <div class="abs footer-rule" style="left:335px"></div>
    <ul class="abs contacts">
      <li><svg width="20" height="20" viewBox="0 0 20 20"><path d="M5 2l3 4-2 2c1 3 3 5 6 6l2-2 4 3-2 3C9 18 2 11 2 4z" fill="var(--gold)"/></svg>+46 70 555 01 23</li>
      <li><svg width="20" height="14" viewBox="0 0 20 14"><rect width="20" height="14" fill="var(--gold)"/><path d="M0 0l10 8 10-8" fill="none" stroke="var(--footer)" stroke-width="1.4"/></svg>info@zenfroloop.com</li>
      <li><svg width="20" height="20" viewBox="0 0 20 20" fill="none" stroke="var(--gold)" stroke-width="1.5"><circle cx="10" cy="10" r="8.5"/><ellipse cx="10" cy="10" rx="3.5" ry="8.5"/><path d="M1.5 10h17M3 5.5h14M3 14.5h14"/></svg>zenfroloop.com</li>
    </ul>
    <div class="abs footer-rule" style="left:569px"></div>
    <p class="abs launch-label">— BEGRÄNSAD LANSERING —</p>
    <div class="abs launch-box">SOMMAREN 2026</div>
    <p class="abs launch-note">Säkra din tilldelning<br>i tid och möt efterfrågan.</p>
  </footer>

</main>
</body>
</html>
```